Business Card Design for a Personal Trainer

I need a business card design for my job as a personal trainer. It should have a unique, modern and exclusive design. On the front there should be only my logo with my name and my job. 0163/2918374 Tobias Kellinger Lindenfeldweg 14 80412 Munich Germany The most important contact information is the web adress. it can be bigger than the rest, but its not necessary. The card should be 8,5cmx5,5cm big. Font: Roboto. Colors: black, white, gray, 56c1ff.

```html
<!DOCTYPE html>
<html lang="de">
<head>
<meta charset="utf-8">
<title>Tobias Kellinger – Personal Trainer Business Card</title>
<link href="https://fonts.googleapis.com/css2?family=Roboto:wght@300;400;500&display=swap" rel="stylesheet">
<style>
  :root {
    --stage: #2b2f36;
    --black: #0d0d0d;
    --white: #ffffff;
    --paper: #f1f1f1;
    --gray: #8a8f96;
    --accent: #56c1ff;
    --photo-dark: #1e2230;
    --photo-mid: #4a5066;
  }
  * { box-sizing: border-box; margin: 0; padding: 0; }
  html, body {
    width: 1200px; height: 900px; overflow: hidden;
    background: var(--stage);
    font-family: "Roboto", sans-serif;
  }
  .canvas {
    width: 1200px; height: 900px;
    display: flex; flex-direction: column; align-items: center; justify-content: center;
    gap: 48px;
  }
  .card {
    position: relative;
    width: 620px; height: 401px;
    overflow: hidden;
    box-shadow: 0 12px 30px rgba(0,0,0,.45);
  }

  /* Front */
  .card-front { background: var(--black); }
  .trainer-photo {
    position: absolute; left: 50%; top: 0;
    width: 260px; height: 300px; transform: translateX(-50%);
    background: radial-gradient(ellipse at 50% 35%, #6b6b6b 0%, #3a3a3a 45%, rgba(13,13,13,0) 75%);
  }
  .front-lockup {
    position: absolute; left: 0; right: 0; bottom: 70px;
    text-align: center; color: var(--white);
  }
  .brand-name {
    font-size: 42px; font-weight: 400; letter-spacing: 1px; text-transform: uppercase;
  }
  .job-title {
    display: flex; align-items: center; justify-content: center; gap: 12px;
    margin-top: 6px; font-size: 15px; font-weight: 300; letter-spacing: 6px; text-transform: uppercase;
  }
  .job-title::before, .job-title::after {
    content: ""; width: 70px; height: 1px; background: currentColor;
  }

  /* Back */
  .card-back { background: var(--paper); }
  .card-back svg.shape { position: absolute; inset: 0; }
  .back-lockup {
    position: absolute; right: 60px; top: 70px;
    text-align: center; color: var(--black);
  }
  .back-lockup .brand-name { font-size: 32px; }
  .back-lockup .job-title { font-size: 12px; letter-spacing: 5px; }
  .back-lockup .job-title::before, .back-lockup .job-title::after { width: 50px; }
  .contact-block {
    position: absolute; left: 40px; bottom: 36px; color: var(--white);
  }
  .contact-name {
    color: var(--accent); font-size: 26px; font-weight: 400; margin-bottom: 18px;
  }
  .contact-list { list-style: none; }
  .contact-list li {
    display: flex; align-items: center; gap: 10px;
    font-size: 17px; font-weight: 400; line-height: 1.55;
  }
  .contact-icon { width: 16px; height: 16px; flex: none; }
</style>
</head>
<body>
<main class="canvas">

  <section class="card card-front">
    <div class="trainer-photo" role="img" aria-label="Black and white portrait photo of the trainer with arms crossed"></div>
    <div class="front-lockup">
      <div class="brand-name">Tobias Kellinger</div>
      <div class="job-title">Personal Trainer</div>
    </div>
  </section>

  <section class="card card-back">
    <svg class="shape" width="620" height="401" viewBox="0 0 620 401">
      <defs>
        <linearGradient id="lakeTones" x1="0" y1="0" x2="0" y2="1">
          <stop offset="0" stop-color="#5a6075"/>
          <stop offset="0.5" stop-color="#2f3446"/>
          <stop offset="1" stop-color="#161922"/>
        </linearGradient>
      </defs>
      <path class="accent-band" d="M0 105 Q 300 300 620 310 L620 401 L0 401 Z" fill="var(--accent)"/>
      <path d="M0 120 Q 300 318 620 330 L620 401 L0 401 Z" fill="url(#lakeTones)" role="img" aria-label="Photo of a person standing at a lakeshore under a cloudy sky"/>
    </svg>

    <div class="back-lockup">
      <div class="brand-name">Tobias Kellinger</div>
      <div class="job-title">Personal Trainer</div>
    </div>

    <div class="contact-block">
      <div class="contact-name">Tobias Kellinger</div>
      <ul class="contact-list">
        <li>
          <svg class="contact-icon" viewBox="0 0 16 16"><circle cx="8" cy="8" r="8" fill="var(--accent)"/><path d="M5 4.5l1.5-.5 1 2-1 .8a5 5 0 0 0 2.7 2.7l.8-1 2 1-.5 1.5c-3.5.3-6.8-3-6.5-6.5z" fill="var(--white)"/></svg>
          0163/2918374
        </li>
        <li>
          <svg class="contact-icon" viewBox="0 0 16 16"><circle cx="8" cy="8" r="8" fill="var(--accent)"/><rect x="4" y="5" width="8" height="6" rx="1" fill="var(--white)"/><path d="M4 5.5l4 3 4-3" stroke="var(--accent)" fill="none"/></svg>
          training@kellinger-coaching.de
        </li>
        <li>
          <svg class="contact-icon" viewBox="0 0 16 16"><circle cx="8" cy="8" r="8" fill="var(--accent)"/><circle cx="8" cy="8" r="4" stroke="var(--white)" fill="none"/><path d="M4 8h8M8 4c-2 2.5-2 5.5 0 8M8 4c2 2.5 2 5.5 0 8" stroke="var(--white)" fill="none" stroke-width=".8"/></svg>
          www.kellinger-coaching.de
        </li>
      </ul>
    </div>
  </section>

</main>
</body>
</html>
```